Cat-products company needs smart, yet endearing, business card

We need a business card design for a new, but up-and-running, business based in Honolulu, Hawaii. The business is Purrlane Nest Co. Our first product is the most environmentally-friendly cat grass kit ever seen on the planet. Future products, currently in the R&D phase, will include a variety of exciting cat scratchers. We also do consulting work to help apartment-dwellers make their home more cat-friendly and, in the future, plan on doing full, custom installs of structure to create high walkways for cats.

Target Market(s)

Middle-aged, apartment-dwelling, middle-class workers who own 1 or more cats and who dote on them.

Industry/Entity Type

Pet Care

Contact Information for Business Card

A striking, professional, yet warm and friendly design is what we're after.

Font styles to use
Serif
Sans Serif
Other font styles liked:
• Comfortaa

Colors

Designer to choose colors to be used in the design.

Requirements
Must have
• The company logo: (see attachment)
• The company name: Purrlane Nest Co
• The web address: www.purrlanenestco.example
• Email: support@purrlanenestco.example
• Phone: +1 (808) 555 0172
• Update (Fri Jun 30 3017 7:45pm Hawaii Time) I would like, is possible, uploaded picture of the cat grass kit on the back of the card with some text along the lines of: Purrlane Nest Co - Where The Freshest Kitty Sprouts Begin
Nice to have
• A cat picture, cartoon, real or silhouette that illustrates cats in action and/or relaxing; ie using the apartment space to live, play and relax in and being well-contented.
• Most of the website is done in the font: Comfortaa. It might be nice to continue using this for brand consistency.
Should not have
• Hard-to-read fonts.

```html
<!DOCTYPE html>
<html lang="en">
<head>
<meta charset="utf-8">
<title>Purrlane Nest Co – Business Card</title>
<link href="https://fonts.googleapis.com/css2?family=Comfortaa:wght@700&family=Montserrat:wght@400&family=Tinos:wght@700&display=swap" rel="stylesheet">
<style>
  :root {
    --page: #f2f2f2;
    --card-front: #bbbcbe;
    --ink: #111111;
    --brand-brown: #4e2a22;
    --brand-gold: #f5b01a;
    --shadow: rgba(0, 0, 0, 0.35);
  }
  html, body {
    margin: 0;
    padding: 0;
    width: 1200px;
    height: 927px;
    overflow: hidden;
    background: var(--page);
  }
  .canvas {
    position: relative;
    width: 1200px;
    height: 927px;
  }
  .card {
    position: absolute;
    left: 282px;
    width: 618px;
    height: 352px;
    border-radius: 16px;
    overflow: hidden;
    box-shadow: 10px 10px 12px var(--shadow);
  }
  .card--front { top: 78px; background: var(--card-front); }
  .card--back { top: 497px; }

  .brand-lockup {
    position: absolute;
    left: 40px;
    top: 110px;
    width: 164px;
    height: 146px;
  }
  .brand-lockup__dot {
    position: absolute;
    left: 50%;
    top: 0;
    width: 74px;
    height: 74px;
    margin-left: -37px;
    border-radius: 50%;
    background: var(--brand-brown);
  }
  .brand-lockup__name {
    position: absolute;
    left: 0;
    right: 0;
    top: 86px;
    text-align: center;
    font-family: "Comfortaa", sans-serif;
    font-weight: 700;
    font-size: 22px;
    line-height: 26px;
    color: var(--brand-brown);
  }

  .divider {
    position: absolute;
    left: 252px;
    top: 111px;
    width: 1.5px;
    height: 145px;
    background: var(--ink);
  }

  .company-name {
    position: absolute;
    left: 306px;
    top: 124px;
    margin: 0;
    font-family: "Tinos", "Times New Roman", serif;
    font-weight: 700;
    font-size: 24px;
    line-height: 30px;
    color: var(--ink);
  }
  .contact-list {
    position: absolute;
    left: 306px;
    top: 178px;
    margin: 0;
    padding: 0;
    list-style: none;
    font-family: "Montserrat", sans-serif;
    font-size: 15px;
    color: var(--ink);
  }
  .contact-list li {
    display: flex;
    align-items: center;
    height: 20.5px;
    white-space: nowrap;
  }
  .contact-list svg {
    width: 11px;
    height: 11px;
    margin-right: 16px;
    flex: none;
  }

  .back-photo {
    position: absolute;
    inset: 0;
    background:
      radial-gradient(ellipse 34% 48% at 30% 62%, #f4efe9 0%, rgba(244,239,233,0) 100%),
      radial-gradient(ellipse 32% 50% at 64% 52%, #f2dfc9 0%, rgba(242,223,201,0) 100%),
      linear-gradient(180deg, #979597 0%, #a9a7a8 40%, #c9c6c3 75%, #d4d1ce 100%);
  }
  .back-name {
    position: absolute;
    left: 0;
    right: 0;
    bottom: 16px;
    text-align: center;
    font-family: "Comfortaa", sans-serif;
    font-weight: 700;
    font-size: 34px;
    color: var(--brand-gold);
  }
</style>
</head>
<body>
<div class="canvas">

  <section class="card card--front">
    <div class="brand-lockup">
      <div class="brand-lockup__dot"></div>
      <div class="brand-lockup__name">Purrlane<br>Nest Co</div>
    </div>
    <div class="divider"></div>
    <h1 class="company-name">Purrlane Nest Co</h1>
    <ul class="contact-list">
      <li>
        <svg viewBox="0 0 12 12" aria-hidden="true"><g fill="none" stroke="var(--ink)" stroke-width="1"><circle cx="6" cy="6" r="5"/><ellipse cx="6" cy="6" rx="2.2" ry="5"/><path d="M1 6 H11 M1.8 3.5 H10.2 M1.8 8.5 H10.2"/></g></svg>
        www.purrlanenestco.example
      </li>
      <li>
        <svg viewBox="0 0 12 12" aria-hidden="true"><rect x="0.8" y="2.3" width="10.4" height="7.4" fill="none" stroke="var(--ink)" stroke-width="1.3"/><path d="M0.8 2.5 L6 6.5 L11.2 2.5" fill="none" stroke="var(--ink)" stroke-width="1.3"/></svg>
        support@purrlanenestco.example
      </li>
      <li>
        <svg viewBox="0 0 12 12" aria-hidden="true"><path d="M2.5 1 L4.5 1 L5 3.5 L3.8 4.3 Q5 7 7.7 8.2 L8.5 7 L11 7.5 L11 9.5 Q10.5 11 9 11 Q1 10 1 3 Q1 1.5 2.5 1 Z" fill="var(--ink)"/></svg>
        +1 (808) 555 0172
      </li>
    </ul>
  </section>

  <section class="card card--back">
    <div class="back-photo" role="img" aria-label="Soft, faded photo of two fluffy kittens, one white and one ginger, lying side by side on a grey blanket"></div>
    <div class="back-name">Purrlane Nest Co</div>
  </section>

</div>
</body>
</html>
```